Halvorn - Refresh the look and feel of an existing website

We currently have an existing website www.halvornworldadvisory.example however it needs a more refreshed 'look and feel'. We are a professional consultancy that works with large corporate organisations and government. Our 'tag line' is A New Way of Thinking. We want the site to communicate "Innovation" and Leading Edge Thinking.

Target Market(s)

Corporate and Professional Clients - Organisation and Business Change

Industry/Entity Type

Management Consulting

Number of Pages Required

1 page

Font styles to use
Sans Serif

Requirements
Must have
• Must have a professional Corporate look and feel. Header 'imagery' is ok but boxes on front page need changing ... along with the words. The focus on home page needs to 'call out' 3 main consulting areas:-
• - Change & Transformation Specialists
• - Innovative Solutions
• - Digital Transformation
• Tag Line for business is ... A New Way of Thinking (Highlighting Halvorn as 'Thought Leaders' in business)
Nice to have
• Less "words' more imagery. Possibly an area for a 'video' or recent articles/blogs on the front page. Needs to have more of an 'interactive' feel. We are open to suggestions.
Should not have
• NA

```html
<!DOCTYPE html>
<html lang="en">
<head>
<meta charset="utf-8">
<title>Halvorn Global Solutions</title>
<link href="https://fonts.googleapis.com/css2?family=Open+Sans:wght@400;600&display=swap" rel="stylesheet">
<style>
:root{
  --red:#c0170a;
  --navy:#243d57;
  --blue:#0f4d9c;
  --band:rgba(24,86,166,.88);
  --ink:#222;
  --heading:#243d57;
  --line:#999;
  --white:#fff;
}
*{margin:0;padding:0;box-sizing:border-box}
html,body{width:967px;height:1200px;overflow:hidden;background:var(--white);font-family:'Open Sans',sans-serif;color:var(--ink)}
.page{position:relative;width:967px;height:1200px}
.hero-photo{position:absolute;left:0;top:0;width:967px;height:547px;
  background:linear-gradient(100deg,#eef3f6 0%,#e3ecf2 35%,#c9d4de 55%,#4d5f78 72%,#22324f 88%,#1d2c4a 100%)}
.header{position:absolute;left:0;top:0;width:967px;height:88px;background:rgba(255,255,255,.82);border-bottom:1px solid #888}
.brand{position:absolute;left:128px;top:22px;display:flex;align-items:center;gap:10px}
.brand-dot{width:44px;height:44px;border-radius:50%;background:var(--navy)}
.brand-name{font-weight:600;font-size:19px;color:var(--navy);line-height:1.05;letter-spacing:.5px}
.brand-name small{display:block;font-size:9.5px;letter-spacing:.8px}
.nav{position:absolute;right:128px;top:37px;display:flex;font-size:13px}
.nav a{color:var(--ink);text-decoration:none;padding:0 13px;border-left:1px solid #555;line-height:18px}
.nav a:first-child{border-left:none;color:var(--red)}
.nav a:last-child{padding-right:0}
.hero-text{position:absolute;left:128px;top:210px}
.hero-text h1{font-weight:400;font-size:30px;color:var(--red);letter-spacing:.3px}
.hero-text p{margin-top:12px;font-size:21px;line-height:26px;color:var(--navy)}
.btn-learn{position:absolute;left:128px;top:330px;width:141px;height:35px;background:var(--blue);color:var(--white);font-size:13.5px;display:flex;align-items:center;padding-left:19px;gap:14px}
.cards{position:absolute;left:128px;top:597px;display:flex;gap:21px}
.card{position:relative;width:223px;height:158px}
.card-photo{position:absolute;inset:0}
.card-label{position:absolute;left:0;bottom:0;width:100%;height:37px;background:var(--band);color:var(--white);font-size:12.5px;font-weight:600;display:flex;align-items:center;justify-content:center}
.subscribe-title{position:absolute;left:0;top:802px;width:967px;text-align:center;font-size:25px;color:var(--heading)}
.field{position:absolute;top:860px;width:224px;height:40px;border:1px solid #999;font-size:12.5px;padding-left:15px;display:flex;align-items:center}
.btn-subscribe{position:absolute;left:616px;top:860px;width:222px;height:40px;background:var(--red);color:var(--white);font-size:17px;font-weight:600;display:flex;align-items:center;justify-content:center;gap:16px;letter-spacing:.5px}
.footer{position:absolute;left:0;top:956px;width:967px;height:212px;background:var(--navy);color:var(--white)}
.col{position:absolute;top:23px}
.col h2{font-weight:400;font-size:22px;margin-bottom:14px}
.col p{font-size:12px;line-height:19px;width:230px}
.col .more{display:block;margin-top:14px;font-size:8.5px;font-style:italic;text-decoration:underline;color:var(--white)}
.col ul{list-style:none;font-size:12px;line-height:19px}
.col li{display:flex;align-items:center;gap:6px}
.contact li{line-height:25.5px;gap:11px}
.bottom{position:absolute;left:128px;top:1177px;width:711px;display:flex;justify-content:space-between;align-items:center;font-size:8.5px}
.social{display:flex;gap:8px}
.social span{width:12px;height:12px;border-radius:50%;background:var(--navy)}
</style>
</head>
<body>
<div class="page">
  <div class="hero-photo" role="img" aria-label="Two business consultants reviewing a tablet together in a bright office"></div>

  <header class="header">
    <div class="brand"><span class="brand-dot"></span><div class="brand-name">HALVORN<small>GLOBAL SOLUTIONS</small></div></div>
    <nav class="nav"><a>Home</a><a>About Us</a><a>Services</a><a>Solutions</a><a>What’s New</a><a>Contact Us</a></nav>
  </header>

  <section class="hero-text">
    <h1>A NEW WAY OF THINKING</h1>
    <p>To Succeed in a complex world,<br>You need a new way of thinking.</p>
  </section>
  <div class="btn-learn">Learn More
    <svg width="9" height="14" viewBox="0 0 9 14"><path d="M1 1l6 6-6 6" fill="none" stroke="#fff" stroke-width="1.6"/></svg>
  </div>

  <section class="cards">
    <div class="card"><div class="card-photo" role="img" aria-label="Consultant working at a screen with management planning notes" style="background:linear-gradient(135deg,#6a7788,#c9ccd0 60%,#e6e6e2)"></div><div class="card-label">Change &amp; Transformation Specialists</div></div>
    <div class="card"><div class="card-photo" role="img" aria-label="Hands holding a tablet showing innovation charts" style="background:linear-gradient(135deg,#e9edf0,#2e9ab0 50%,#7e98b8)"></div><div class="card-label">Innovative Solutions</div></div>
    <div class="card"><div class="card-photo" role="img" aria-label="Businessman with a digital transformation network graphic" style="background:linear-gradient(135deg,#8fa6be,#2a3c5a 55%,#b7c3cf)"></div><div class="card-label">Digital Transformation</div></div>
  </section>

  <h2 class="subscribe-title" style="font-weight:400">Subscribe Now For Our Latest News</h2>
  <div class="field" style="left:128px">Email</div>
  <div class="field" style="left:372px">Name</div>
  <div class="btn-subscribe">SUBSCRIBE
    <svg width="10" height="16" viewBox="0 0 10 16"><path d="M1 1l7 7-7 7" fill="none" stroke="#fff" stroke-width="1.8"/></svg>
  </div>

  <footer class="footer">
    <div class="col" style="left:128px">
      <h2>About Us</h2>
      <p>Our strength is our people - highly skilled, dedicated specialists who have proven experience delivering the outcomes that our clients need.</p>
      <a class="more">Read More &gt;&gt;</a>
    </div>
    <div class="col" style="left:376px">
      <h2>Our Services</h2>
      <ul>
        <li><svg width="6" height="9" viewBox="0 0 6 9"><path d="M1 1l3.5 3.5L1 8" fill="none" stroke="#fff"/></svg>Strategy and Design</li>
        <li><svg width="6" height="9" viewBox="0 0 6 9"><path d="M1 1l3.5 3.5L1 8" fill="none" stroke="#fff"/></svg>Transformation</li>
        <li><svg width="6" height="9" viewBox="0 0 6 9"><path d="M1 1l3.5 3.5L1 8" fill="none" stroke="#fff"/></svg>Change &amp; Culture</li>
        <li><svg width="6" height="9" viewBox="0 0 6 9"><path d="M1 1l3.5 3.5L1 8" fill="none" stroke="#fff"/></svg>Organisational Development</li>
        <li><svg width="6" height="9" viewBox="0 0 6 9"><path d="M1 1l3.5 3.5L1 8" fill="none" stroke="#fff"/></svg>Project Management</li>
        <li><svg width="6" height="9" viewBox="0 0 6 9"><path d="M1 1l3.5 3.5L1 8" fill="none" stroke="#fff"/></svg>Organisational Efficiency</li>
        <li><svg width="6" height="9" viewBox="0 0 6 9"><path d="M1 1l3.5 3.5L1 8" fill="none" stroke="#fff"/></svg>Specialist Placements</li>
      </ul>
    </div>
    <div class="col contact" style="left:616px">
      <h2>Get in touch</h2>
      <ul>
        <li><svg width="11" height="11" viewBox="0 0 12 12"><path d="M2 1l2 0 1 3-1.5 1a7 7 0 003.5 3.5L8 7l3 1v2c0 1-1 1.5-2 1.5A9 9 0 01.5 3C.5 2 1 1 2 1z" fill="#fff"/></svg>1300 000 118 (Aus)</li>
        <li><svg width="11" height="11" viewBox="0 0 12 12"><path d="M2 1l2 0 1 3-1.5 1a7 7 0 003.5 3.5L8 7l3 1v2c0 1-1 1.5-2 1.5A9 9 0 01.5 3C.5 2 1 1 2 1z" fill="#fff"/></svg>0800 080 118 (NZ)</li>
        <li><svg width="11" height="11" viewBox="0 0 12 12"><path d="M2 1l2 0 1 3-1.5 1a7 7 0 003.5 3.5L8 7l3 1v2c0 1-1 1.5-2 1.5A9 9 0 01.5 3C.5 2 1 1 2 1z" fill="#fff"/></svg>1300 000 118 (Intl)</li>
        <li><svg width="11" height="9" viewBox="0 0 12 9"><rect width="12" height="9" fill="#fff"/><path d="M0 0l6 5 6-5" fill="none" stroke="#243d57"/></svg>info@halvornworldadvisory.example</li>
      </ul>
    </div>
  </footer>

  <div class="bottom">
    <span>Copyright © 2014 Halvorn Global Solutions</span>
    <div class="social"><span></span><span></span><span></span><span></span></div>
  </div>
</div>
</body>
</html>
```